Best in class cloud software provider for retailers needs a new business card design to reflect prod

We are a software company based out of Chicago selling into retailers. We have a new website and marketing collateral that support our new product designs. We are obsessed with simplicity, ease of use, and having a really powerful product set. We have two products as noted on our website - www.plumvector.example - one is a retail task management product and the other is a Help Ticketing product.

At PlumVector we are passionate about creating the best Retail Task Management system in the industry. We bring more than 20 years of retail operations, Workforce Management and Retail Task experience and have a set of web and mobile software features that no one else has. PlumVector enables you to plan and distribute work throughout your organization and ensure it gets done.

We need a new business card design that reflects our new branding, message and approach.

I've attached a few documents that help support what we are building and how our colors look.

There may be additional future work if this goes well.

Thanks,
Brian

President

Target Market(s)

We sell into retailers and are a software company

Industry/Entity Type

Software

Contact Information for Business Card

The card must have

Name
title
address
tele
email
PlumVector logo (someplace)

So for example

It would have for me

Brian Okafor
President
47 North Garnet Ave. Suite 310
Chicago, IL 60618
3127814063
bokafor@plumvector.example

Requirements
Must have
• We need to cards for 5 different people - same design different names etc
Nice to have
• should reflect our colors and product and website - be creative - ease of use, simplicity, and power is what the product is about - but we are very forward PlumVector and hear all the time that our product is gorgeous. The font should be consistent with our website, and marketing one pager included
Should not have
• Strange or unfamiliar colors or fonts...

```html
<!DOCTYPE html>
<html lang="en">
<head>
<meta charset="utf-8">
<title>PlumVector Business Card</title>
<link rel="stylesheet" href="https://fonts.googleapis.com/css2?family=Open+Sans:wght@400;600;700&display=swap">
<style>
  :root {
    --bg: #2b2b2d;
    --card: #030303;
    --brand-blue: #2180b3;
    --accent-orange: #f26b21;
    --text-white: #ffffff;
  }
  * { margin: 0; padding: 0; box-sizing: border-box; }
  html, body { width: 1200px; height: 900px; overflow: hidden; }
  body {
    background: var(--bg);
    font-family: "Open Sans", Arial, sans-serif;
    position: relative;
  }
  .card {
    position: absolute;
    width: 640px;
    height: 366px;
    border-radius: 20px;
    overflow: hidden;
    background: var(--card);
    box-shadow: 0 14px 30px rgba(0,0,0,0.45);
  }
  .card-front { left: 70px; top: 50px; }
  .card-back { left: 490px; top: 484px; }
  .card-wave { position: absolute; inset: 0; width: 100%; height: 100%; }

  .wordmark {
    position: absolute;
    color: var(--brand-blue);
    font-weight: 700;
    letter-spacing: -1px;
    line-height: 1;
  }
  .card-front .wordmark { left: 110px; top: 120px; font-size: 84px; }
  .card-back .wordmark { left: 40px; top: 118px; font-size: 64px; }

  .website {
    position: absolute;
    left: 70px; bottom: 22px;
    color: var(--text-white);
    font-size: 16px;
    font-weight: 400;
  }

  .holder {
    position: absolute;
    right: 34px; top: 40px;
    text-align: right;
  }
  .holder-name {
    color: var(--brand-blue);
    font-size: 22px;
    font-weight: 700;
    line-height: 1.1;
  }
  .holder-title {
    color: var(--accent-orange);
    font-size: 13px;
    font-weight: 600;
  }
  .divider {
    position: absolute;
    left: 40px; right: 34px; top: 210px;
    height: 1.5px;
    background: var(--brand-blue);
  }

  .contact {
    position: absolute;
    left: 40px; top: 228px;
    list-style: none;
    color: var(--brand-blue);
    font-size: 14px;
    font-weight: 600;
    line-height: 20px;
  }
  .contact li { display: flex; align-items: flex-start; gap: 8px; }
  .contact-icon { width: 12px; height: 12px; margin-top: 4px; flex: none; }
  .contact-address { padding-left: 20px; }
</style>
</head>
<body>

<section class="card card-front">
  <svg class="card-wave" viewBox="0 0 640 366" preserveAspectRatio="none" aria-hidden="true">
    <path fill="var(--accent-orange)" d="M0,286 C60,346 160,320 300,268 C450,214 600,216 640,146 L640,366 L0,366 Z"/>
    <path fill="var(--card)" d="M0,294 C60,352 160,328 300,276 C450,222 600,224 640,156 L640,366 L0,366 Z"/>
    <path fill="var(--brand-blue)" d="M0,300 C60,358 160,334 300,282 C450,228 600,230 640,162 L640,366 L0,366 Z"/>
  </svg>
  <div class="wordmark">PlumVector</div>
  <div class="website">www.plumvector.example</div>
</section>

<section class="card card-back">
  <svg class="card-wave" viewBox="0 0 640 366" preserveAspectRatio="none" aria-hidden="true">
    <path fill="var(--accent-orange)" d="M180,366 C300,350 360,290 440,230 C520,170 600,168 640,182 L640,366 Z"/>
    <path fill="var(--card)" d="M190,366 C310,356 370,298 448,240 C524,182 600,178 640,192 L640,366 Z"/>
    <path fill="var(--brand-blue)" d="M196,366 C316,360 376,304 454,246 C528,190 602,186 640,200 L640,366 Z"/>
  </svg>

  <div class="wordmark">PlumVector</div>

  <div class="holder">
    <div class="holder-name">Brian Okafor</div>
    <div class="holder-title">President</div>
  </div>

  <div class="divider"></div>

  <ul class="contact">
    <li>
      <svg class="contact-icon" viewBox="0 0 12 12" aria-hidden="true"><path fill="var(--accent-orange)" d="M2,0.5 L4.5,0.5 L5.2,3.4 L3.7,4.6 C4.4,6.1 5.9,7.6 7.4,8.3 L8.6,6.8 L11.5,7.5 L11.5,10 C11.5,11 10.6,11.5 9.8,11.5 C4.8,11 1,7.2 0.5,2.2 C0.5,1.3 1,0.5 2,0.5 Z"/></svg>
      <span>312 781 4063</span>
    </li>
    <li>
      <svg class="contact-icon" viewBox="0 0 12 12" aria-hidden="true"><rect x="0.8" y="2.2" width="10.4" height="7.6" fill="none" stroke="var(--accent-orange)" stroke-width="1.4"/><path d="M1,2.6 L6,6.6 L11,2.6" fill="none" stroke="var(--accent-orange)" stroke-width="1.4"/></svg>
      <span>bokafor@plumvector.example</span>
    </li>
    <li>
      <svg class="contact-icon" viewBox="0 0 12 12" aria-hidden="true"><circle cx="6" cy="6" r="5.2" fill="none" stroke="var(--accent-orange)" stroke-width="1.3"/><path d="M0.8,6 H11.2 M6,0.8 C3.5,3.5 3.5,8.5 6,11.2 M6,0.8 C8.5,3.5 8.5,8.5 6,11.2" fill="none" stroke="var(--accent-orange)" stroke-width="1"/></svg>
      <span>www.plumvector.example</span>
    </li>
    <li class="contact-address">47 North Garnet Ave.</li>
    <li class="contact-address">Suite 310 Chicago, IL 60618</li>
  </ul>
</section>

</body>
</html>
```